New custom software business needs a Wordpress site

We need a Wordpress site for a new company based out of Chicago called 'Vellora Consulting'. Using a mix of on and off-shore resources we build custom software solutions, mainly focusing on small to medium sized companies. We help our customers "aspire" to do great things.
We have a basic site up here: https://brindlewave.example/. We worked on the content for it but not the branding. For now, this houses all the pages (except for a Contact Us page we'll be adding soon) for the foreseeable future.
We also have a new logo (attached) that we'd like to base the styling/colors on.
Target Market(s)
Small to medium sized companies that require tech resources
Industry/Entity Type
Software
Nice to have
- Teamwork, tech, professional but not elitist

```html
<!DOCTYPE html>
<html lang="en">
<head>
<meta charset="utf-8">
<title>Vellora Consulting</title>
<link rel="stylesheet" href="https://fonts.googleapis.com/css2?family=Audiowide&family=Poppins:ital,wght@0,300;0,400;0,500;1,400&display=swap">
<style>
:root{
  --navy:#0b1f3f;
  --royal:#0d56ad;
  --royal-deep:#0a4a98;
  --sky:#75a6d6;
  --pale:#e8eff7;
  --ink:#1f2a38;
  --grey:#7b8593;
  --white:#ffffff;
  --line:#c6d7ea;
}
*{margin:0;padding:0;box-sizing:border-box}
html,body{width:1200px;height:3984px;overflow:hidden}
body{position:relative;font-family:"Poppins",sans-serif;color:var(--ink);background:var(--white)}
.abs{position:absolute}
.display{font-family:"Audiowide",sans-serif;font-weight:400;letter-spacing:1px}
.center{text-align:center}

/* header + hero */
.hero{left:0;top:0;width:1200px;height:700px;background:linear-gradient(160deg,#223a5e 0%,#132a4e 45%,#0a1c3a 100%)}
.site-header{left:0;top:0;width:1200px;height:90px;background:rgba(10,22,44,.55)}
.brand{left:62px;top:22px;display:flex;align-items:center;gap:12px;color:var(--white)}
.brand-dot{width:40px;height:40px;border-radius:50%;background:var(--sky)}
.brand-name{font-family:"Audiowide",sans-serif;font-size:26px;line-height:1}
.brand-sub{font-size:10px;letter-spacing:3px;color:var(--sky);margin-top:3px}
.nav{right:62px;top:34px;display:flex;gap:26px;font-size:14px;color:var(--white)}
.nav .active{color:var(--sky)}
.hero-title{left:0;width:1200px;top:268px;font-size:56px;color:var(--white)}
.hero-sub{left:340px;width:520px;top:332px;font-size:17px;line-height:27px;color:#dbe5f2;font-weight:300}
.btn{display:inline-block;font-family:"Audiowide",sans-serif;color:var(--white);background:var(--royal);font-size:17px;letter-spacing:1px;text-align:center}
.hero-btn{left:507px;top:411px;width:183px;height:43px;line-height:43px}
.hero-notch{left:585px;top:630px;width:30px;height:30px;border-radius:50%;background:var(--royal)}

/* section headings */
.sec-title{font-size:38px;color:var(--royal);line-height:46px}
.divider{display:flex;align-items:center;gap:14px;justify-content:center}
.divider i{display:block;width:88px;height:2px;background:var(--line)}
.divider b{display:block;width:18px;height:18px;border-radius:50%;background:var(--royal)}

/* services */
.service{width:330px;text-align:center}
.service-icon{width:128px;height:128px;margin:0 auto}
.service h3{font-family:"Audiowide",sans-serif;font-weight:400;font-size:21px;line-height:28px;margin-top:34px;color:var(--ink)}
.service p{font-size:13px;line-height:26px;color:var(--grey);margin-top:14px}
.read-more{display:inline-block;margin-top:14px;font-family:"Audiowide",sans-serif;font-size:12px;color:#5a8cc4;text-decoration:underline}
.vline{left:617px;top:946px;width:1px;height:376px;background:#e2e8f0}

/* about band */
.about-text{left:62px;top:1582px;width:545px;color:var(--white);font-size:13px;line-height:22.5px;font-weight:300}
.about-text p{margin-bottom:13px}
.about-link{font-style:italic;color:var(--sky);text-decoration:underline;font-size:15px;line-height:26px}
.about-btn{left:60px;top:1996px;width:183px;height:43px;line-height:43px;background:var(--sky);font-size:17px}
.about-photo{left:657px;top:1600px;width:518px;height:441px;border-radius:6px;background:radial-gradient(ellipse at 50% 45%,#3a4656 0%,#23303f 45%,rgba(13,86,173,0) 75%)}

/* clients */
.clients{left:0;top:2211px;width:1200px;height:355px;background:var(--pale)}
.client{top:2406px;width:193px;height:80px;background:var(--white);border-radius:6px;display:flex;align-items:center;justify-content:center;gap:8px;font-family:"Poppins",sans-serif;font-weight:500;font-size:22px;color:var(--ink)}
.client i{display:block;width:14px;height:14px;border-radius:50%;background:var(--royal)}

/* offer cards */
.offer{top:2770px;width:333px}
.offer-img{width:333px;height:233px;background:linear-gradient(135deg,#8c98a6,#566272 60%,#3d4858)}
.offer-corner{right:0;top:0}
.offer h3{font-family:"Audiowide",sans-serif;font-weight:400;font-size:21px;margin-top:30px;color:var(--ink)}
.offer p{font-size:13px;line-height:22px;color:var(--grey);margin-top:16px;width:270px}
.offer hr{border:0;height:3px;background:var(--pale);margin-top:16px}

/* testimonial */
.avatar{left:241px;top:3256px;width:118px;height:118px;border-radius:50%;border:4px solid var(--pale);background:linear-gradient(160deg,#d7dde4,#9aa6b3)}
.quote{left:407px;top:3262px;width:490px;font-size:17px;line-height:30px;color:var(--ink)}
.quote-name{left:407px;top:3385px;font-family:"Audiowide",sans-serif;color:var(--royal);font-size:16px}
.quote-bar{left:956px;top:3268px;width:3px;height:104px;background:repeating-linear-gradient(var(--royal) 0 30px,transparent 30px 37px)}

/* footer */
.foot-eyebrow{left:62px;top:3616px;font-size:14px;color:var(--white)}
.foot-title{left:62px;top:3645px;font-size:38px;color:var(--white)}
.foot-dot{left:62px;top:3703px;width:18px;height:18px;border-radius:50%;background:var(--sky)}
.contact-box{left:59px;width:349px;height:48px;border:1.5px solid rgba(255,255,255,.8);display:flex;align-items:center;color:var(--white);font-size:17px}
.contact-box svg{margin:0 14px 0 16px}
.contact-box span{border-left:1px solid rgba(255,255,255,.6);padding-left:14px;line-height:20px}
.foot-col h4{font-family:"Audiowide",sans-serif;font-weight:400;font-size:19px;color:var(--white);margin-bottom:20px}
.foot-col li{list-style:none;font-size:14px;color:var(--white);line-height:30px;padding-left:24px;position:relative}
.foot-col li::before{content:"";position:absolute;left:2px;top:12px;border-left:5px solid transparent;border-right:5px solid transparent;border-bottom:7px solid var(--sky)}
.foot-mark{left:930px;top:3660px;width:200px;height:120px;font-family:"Poppins",sans-serif;font-weight:500;font-size:34px;color:var(--sky);display:flex;align-items:center;justify-content:center}
.copyright{left:0;width:1200px;top:3950px;font-size:13px;color:#cfdcec}
</style>
</head>
<body>

<!-- hero -->
<div class="abs hero" role="img" aria-label="Dim office interior with people working at desks, tinted deep blue"></div>
<svg class="abs" style="left:0;top:590px" width="1200" height="130" viewBox="0 0 1200 130">
  <polygon points="0,13 0,110 590,110" fill="var(--sky)"/>
  <polygon points="0,110 590,110 1200,40 1200,130 0,130" fill="var(--white)"/>
</svg>
<div class="abs hero-notch"></div>

<header class="abs site-header">
  <div class="abs brand"><div class="brand-dot"></div><div><div class="brand-name">VELLORA</div><div class="brand-sub">CONSULTING</div></div></div>
  <nav class="abs nav"><span class="active">Home</span><span>About</span><span>Services</span><span>Why Vellora?</span><span>Vellora Leadership</span><span>Contact Us</span></nav>
</header>

<h1 class="abs hero-title display center">VELLORA CONSULTING</h1>
<p class="abs hero-sub center">Using a mix of on and off-shore resources we build custom software solutions</p>
<a class="abs btn hero-btn">CONTACT US</a>

<!-- services -->
<h2 class="abs sec-title display center" style="left:0;width:1233px;top:753px">SERVICES WE<br>PROVIDE</h2>
<div class="abs divider" style="left:0;width:1233px;top:868px"><i></i><b></b><i></i></div>

<div class="abs vline"></div>
<div class="abs service" style="left:268px;top:932px">
  <svg class="service-icon" viewBox="0 0 128 128">
    <polygon points="64,2 126,126 2,126" fill="#eef3f9"/>
    <rect x="30" y="38" width="68" height="46" rx="3" fill="none" stroke="var(--royal)" stroke-width="3"/>
    <line x1="30" y1="74" x2="98" y2="74" stroke="var(--royal)" stroke-width="3"/>
    <path d="M56 84 L52 96 H76 L72 84" fill="none" stroke="var(--royal)" stroke-width="3"/>
    <circle cx="64" cy="56" r="10" fill="none" stroke="var(--royal)" stroke-width="3"/>
  </svg>
  <h3>CUSTOM SOLUTIONS<br>DELIVERY</h3>
  <p>Vellora offers a range of services focused on helping businesses and organizations deliver software solutions to their customers or users.</p>
  <a class="read-more">READ MORE ▸</a>
</div>
<div class="abs service" style="left:631px;top:932px">
  <svg class="service-icon" viewBox="0 0 128 128">
    <polygon points="64,2 126,126 2,126" fill="#eef3f9"/>
    <circle cx="64" cy="42" r="14" fill="none" stroke="var(--royal)" stroke-width="3" stroke-dasharray="6 3"/>
    <circle cx="64" cy="42" r="6" fill="none" stroke="var(--royal)" stroke-width="3"/>
    <circle cx="46" cy="70" r="6" fill="none" stroke="var(--royal)" stroke-width="3"/>
    <circle cx="64" cy="70" r="6" fill="none" stroke="var(--royal)" stroke-width="3"/>
    <circle cx="82" cy="70" r="6" fill="none" stroke="var(--royal)" stroke-width="3"/>
    <path d="M36 94 V86 a10 10 0 0 1 20 0 V94 M54 94 V86 a10 10 0 0 1 20 0 V94 M72 94 V86 a10 10 0 0 1 20 0 V94 Z" fill="none" stroke="var(--royal)" stroke-width="3"/>
  </svg>
  <h3>STAFF<br>AUGMENTATION</h3>
  <p>Let Vellora help you supplement your existing software development teams with additional resources and expertise. We provided access to experienced</p>
  <a class="read-more">READ MORE ▸</a>
</div>

<!-- about band -->
<svg class="abs" style="left:0;top:1345px" width="1200" height="880" viewBox="0 0 1200 880">
  <polygon points="0,0 1200,18 1200,866 0,766" fill="var(--royal)"/>
  <polygon points="990,82 1200,18 1200,82" fill="var(--sky)"/>
  <polygon points="0,766 0,860 200,790" fill="var(--sky)"/>
  <polygon points="880,400 1100,880 660,880" fill="#1261bb" opacity=".45"/>
</svg>
<h2 class="abs display" style="left:62px;top:1468px;font-size:38px;color:var(--white)">VELLORA CONSULTING</h2>
<div class="abs" style="left:62px;top:1534px;display:flex;align-items:center;gap:16px"><b style="display:block;width:18px;height:18px;border-radius:50%;background:var(--sky)"></b><i style="display:block;width:88px;height:2px;background:var(--sky)"></i></div>
<div class="abs about-text">
  <p>Welcome to Vellora, a software consulting company specializing in serving small to medium size businesses. We understand the unique challenges and opportunities that these companies face, and we are dedicated to helping them succeed through innovative technology solutions.</p>
  <p>Our team of experienced professionals has a diverse range of skills and expertise, making us well-equipped to handle any project, big or small. We specialize in custom software development, working closely with our clients to understand their specific needs and build solutions that meet their requirements.</p>
  <p>From developing web and mobile applications to implementing cloud-based systems and integrating with existing platforms, we have the tools and knowledge to deliver results that drive success. We also offer a range of other services, including IT consulting, project management, and technical support, to help businesses optimize their operations and achieve their goals.</p>
  <p class="about-link">Contact us today to learn more about how we can help your business grow and thrive through the power of technology.</p>
</div>
<a class="abs btn about-btn">CONTACT US</a>
<div class="abs about-photo" role="img" aria-label="Two business people in lounge chairs reviewing a tablet together"></div>

<!-- clients -->
<div class="abs clients"></div>
<h2 class="abs display center" style="left:0;width:1200px;top:2255px;font-size:24px;line-height:31px;color:var(--royal)">HELPING GLOBAL SOFTWARE TEAMS DO<br>MORE WITH LESS, AND DO IT QUICKER.</h2>
<div class="abs divider" style="left:0;width:1200px;top:2342px"><i></i><b></b><i></i></div>
<div class="abs client" style="left:84px"><i></i>Ferrowick</div>
<div class="abs client" style="left:293px"><i></i>Lumetra</div>
<div class="abs client" style="left:502px"><i></i>Osbrant</div>
<div class="abs client" style="left:712px"><i></i>Quillbay</div>
<div class="abs client" style="left:922px"><i></i>Tarnvale</div>

<!-- also we provide -->
<h2 class="abs sec-title display center" style="left:0;width:1200px;top:2632px">ALSO WE PROVIDE</h2>
<div class="abs divider" style="left:0;width:1200px;top:2700px"><i></i><b></b><i></i></div>

<div class="abs offer" style="left:77px">
  <div class="offer-img" style="position:relative" role="img" aria-label="Business team meeting in a glass-walled office">
    <svg class="abs offer-corner" width="110" height="110" viewBox="0 0 110 110"><polygon points="0,0 110,0 110,110" fill="var(--royal)"/><circle cx="80" cy="30" r="12" fill="none" stroke="#fff" stroke-width="2"/></svg>
  </div>
  <h3>IT CONSULTING</h3>
  <p>We help our customers "aspire" to do great things.</p>
  <hr>
</div>
<div class="abs offer" style="left:433px">
  <div class="offer-img" style="position:relative" role="img" aria-label="Presenter at a whiteboard leading a project meeting">
    <svg class="abs offer-corner" width="110" height="110" viewBox="0 0 110 110"><polygon points="0,0 110,0 110,110" fill="var(--royal)"/><rect x="66" y="18" width="28" height="20" rx="2" fill="none" stroke="#fff" stroke-width="2"/></svg>
  </div>
  <h3>PROJECT MANAGEMENT</h3>
  <p>We help our customers "aspire" to do great things.</p>
  <hr>
</div>
<div class="abs offer" style="left:790px">
  <div class="offer-img" style="position:relative" role="img" aria-label="Support agent wearing a headset at a desk">
    <svg class="abs offer-corner" width="110" height="110" viewBox="0 0 110 110"><polygon points="0,0 110,0 110,110" fill="var(--royal)"/><path d="M68 36 v-6 a12 12 0 0 1 24 0 v6" fill="none" stroke="#fff" stroke-width="2"/></svg>
  </div>
  <h3>TECHNICAL SUPPORT</h3>
  <p>We help our customers "aspire" to do great things.</p>
  <hr>
</div>

<!-- testimonial -->
<div class="abs avatar" role="img" aria-label="Portrait of a client"></div>
<p class="abs quote">" Lorem Ipsum has been the industry's standard dummy text ever since the when an unknown printer took a galley of type &nbsp;scrait to "</p>
<div class="abs quote-name">— NORA CASTELLANE</div>
<div class="abs quote-bar"></div>

<!-- footer -->
<svg class="abs" style="left:0;top:3490px" width="1200" height="494" viewBox="0 0 1200 494">
  <polygon points="0,12 1200,0 1200,494 0,494" fill="var(--royal)"/>
  <polygon points="0,12 600,70 0,110" fill="#0f5fb8"/>
  <polygon points="1200,0 800,72 1200,64" fill="var(--sky)"/>
</svg>
<div class="abs" style="left:588px;top:3540px;width:24px;height:24px;border-radius:50%;background:var(--sky)"></div>
<div class="abs foot-eyebrow">LET'S TALK</div>
<h2 class="abs foot-title display">CONTACT US</h2>
<div class="abs foot-dot"></div>
<div class="abs contact-box" style="top:3760px">
  <svg width="20" height="20" viewBox="0 0 24 24"><path d="M6 2 L10 6 L8 9 C9 12 12 15 15 16 L18 14 L22 18 L19 22 C10 21 3 14 2 5 Z" fill="none" stroke="#fff" stroke-width="1.5"/></svg>
  <span>0100 555 246</span>
</div>
<div class="abs contact-box" style="top:3822px">
  <svg width="22" height="18" viewBox="0 0 24 18"><rect x="1" y="1" width="22" height="16" fill="none" stroke="#fff" stroke-width="1.5"/><path d="M1 1 L12 10 L23 1" fill="none" stroke="#fff" stroke-width="1.5"/></svg>
  <span>info@velloraconsulting.example</span>
</div>
<div class="abs foot-col" style="left:451px;top:3662px">
  <h4>SITEMAP</h4>
  <ul><li>Home</li><li>About</li><li>Service</li><li>Why Vellora?</li><li>Vellora Leadership</li><li>Contact Us</li></ul>
</div>
<div class="abs foot-col" style="left:688px;top:3662px">
  <h4>SERVICES</h4>
  <ul><li>Custom Solutions Delivery</li><li>Staff Augmentation</li></ul>
</div>
<div class="abs foot-mark">Vellora</div>
<div class="abs copyright center">©VelloraConsulting - 2022 All rights reserved.</div>

</body>
</html>
```